Kelbrook Tutoring Flyer Design

I need a flyer for a new company based in Samford Valley called 'Kelbrook Tutoring'. We specialise in Mathematics tutoring for students from grade 5 up to grade twelve. We currently have a logo that has purple as its major colour. The final design should convey professionalism, compassion and that education is about maximising peoples possibilities,
Updates

Just thought I would let you know that my slogan is "Maximise your possibilities" and my phone number is 0438260917

Thanks.

My current logo doesn't seem to want to upload

Target Market(s)

The two targets are parents of students in grades 5-12 and students in grades 5-12

Industry/Entity Type

Education

Logo Text

Kelbrook Tutoring

Logo styles of interest
Pictorial/Combination Logo
Abstract Logo
Lettermark Logo
Requirements
Must have
• My slogan is "Maximise your possibilities"
my phone number is 0438260917

```html
<!DOCTYPE html>
<html lang="en">
<head>
<meta charset="UTF-8">
<title>Kelbrook Tutoring Flyer Design</title>
<link rel="stylesheet" href="https://fonts.googleapis.com/css2?family=Baloo+2:wght@800&family=Open+Sans:wght@400;600;700&family=Tinos&display=swap">
<style>
:root{
  --band-left:#2e4a9e;
  --band-right:#5b3a8c;
  --paper:#ffffff;
  --formula:#d6d6dc;
  --headline-a:#2f3fa0;
  --headline-b:#6a2f8c;
  --badge-fill:#fbf06a;
  --badge-core:#fffbd0;
  --badge-ring:#5a3a8c;
  --white:#ffffff;
}
*{margin:0;padding:0;box-sizing:border-box}
html,body{width:933px;height:1200px;overflow:hidden;background:var(--paper)}
.flyer{position:relative;width:933px;height:1200px;background:var(--paper);overflow:hidden;font-family:"Open Sans",Arial,sans-serif}
.formula{position:absolute;font-family:"Tinos","Times New Roman",serif;color:var(--formula);font-size:22px;white-space:nowrap}
.title-band{position:absolute;left:0;top:107px;width:933px;height:201px;
  background:linear-gradient(90deg,var(--band-left),var(--band-right));
  display:flex;align-items:center;justify-content:center}
.brand-name{font-family:"Tinos","Times New Roman",serif;color:var(--white);font-size:74px;font-weight:400;letter-spacing:1px}
.slogan{position:absolute;left:0;top:352px;width:933px;text-align:center;
  font-family:"Baloo 2",Arial,sans-serif;font-weight:800;font-size:66px;line-height:78px;letter-spacing:7px;
  background:linear-gradient(90deg,var(--headline-a),var(--headline-b));
  -webkit-background-clip:text;background-clip:text;color:transparent}
.subject-badge{position:absolute;width:166px;height:166px;border-radius:50%;
  border:4px solid var(--badge-ring);
  background:radial-gradient(circle at 50% 50%,var(--badge-core) 0%,var(--badge-fill) 70%)}
.badge-geometry{left:60px;top:393px}
.badge-medicine{left:712px;top:405px}
.badge-science{left:237px;top:612px}
.badge-computing{left:525px;top:619px}
.info-band{position:absolute;left:0;top:878px;width:933px;height:322px;
  background:linear-gradient(90deg,var(--band-left),var(--band-right));
  color:var(--white);padding:48px 80px 0 80px}
.info-heading{font-size:29px;font-weight:600;margin-bottom:20px}
.info-text{font-size:15.5px;line-height:22px;margin-bottom:14px}
.info-text strong{font-weight:700}
.call-line{font-size:22px;font-weight:700;margin-top:20px}
</style>
</head>
<body>
<div class="flyer">
  <div class="formula" style="left:105px;top:48px">sin x = a;&nbsp; x = (−1)<sup>n</sup> arcsin a + πn,</div>

  <header class="title-band">
    <h1 class="brand-name">Kelbrook Tutoring</h1>
  </header>

  <div class="formula" style="left:40px;top:360px">sin<sup>2</sup> α + cos<sup>2</sup> α = 1</div>
  <div class="formula" style="left:590px;top:328px">cos 2α = cos<sup>2</sup> α − sin<sup>2</sup> α</div>
  <div class="formula" style="left:663px;top:485px">2 sin</div>
  <div class="formula" style="left:130px;top:578px;font-size:16px">tgα ctgα = 1</div>
  <div class="formula" style="left:655px;top:568px">a<sup>log<sub>b</sub> c</sup> = c<sup>log<sub>b</sub> a</sup></div>
  <div class="formula" style="left:310px;top:640px">tg<sup>2</sup>α + 1 = 1 / cos<sup>2</sup> α = sec<sup>2</sup> α</div>
  <div class="formula" style="left:30px;top:663px">log<sub>a</sub> b<sup>r</sup> = r log<sub>a</sub> b</div>
  <div class="formula" style="left:700px;top:668px">= b / sin β = c / sin γ = 2R</div>
  <div class="formula" style="left:68px;top:808px">sin α − sin β = 2 sin (α−β)/2 cos (α+β)/2</div>
  <div class="formula" style="left:530px;top:812px">ctg<sup>2</sup>α + 1 = 1 / sin<sup>2</sup> α = cosec<sup>2</sup>α</div>

  <h2 class="slogan">MAXIMISE<br>YOUR<br>POSSIBILITIES</h2>

  <div class="subject-badge badge-geometry" role="img" aria-label="Geometry set square and compass icon"></div>
  <div class="subject-badge badge-medicine" role="img" aria-label="Stethoscope icon"></div>
  <div class="subject-badge badge-science" role="img" aria-label="Laboratory flasks and test tube icon"></div>
  <div class="subject-badge badge-computing" role="img" aria-label="Laptop computer icon"></div>

  <section class="info-band">
    <h3 class="info-heading">Who knew numbers could be fun?</h3>
    <p class="info-text">At '<strong>Kelbrook Tutoring</strong>', we've made a pledge to ourselves, to help those who have a tough time getting their sums to add up or calculating the right answers to their calculus problems.</p>
    <p class="info-text"><strong>For students in 5th grade up to 12th,</strong> we have your 'problems' covered, with specialised tutoring designed to provide you comprehensive and holistic development in learning mathematics.</p>
    <p class="call-line">Looking to get started?&nbsp; Call us&nbsp; : 0438260917</p>
  </section>
</div>
</body>
</html>
```